Dietitian clinic needs a business card design

We need a business card design for a new dietitian group based in Singapore called "Lantern and Tide". We provide expert, personalised nutrition care to support a wide range of health needs, from chronic conditions to mindful eating. Our team also offers consulting, speaking, and tailored solutions for healthcare providers, organisations, and food services.

Target Market(s)

Adults

Industry/Entity Type

Healthcare

Contact Information for Business Card

Name, position, contact number, email, website address, our logo

Requirements
Nice to have
• Clean, professional but welcoming look

```html
<!DOCTYPE html>
<html lang="en">
<head>
<meta charset="utf-8">
<title>Lantern and Tide – Business Card</title>
<link href="https://fonts.googleapis.com/css2?family=Playfair+Display:wght@400;600;700&family=Libre+Caslon+Text:wght@400&display=swap" rel="stylesheet">
<style>
  :root {
    --backdrop: #5c818c;
    --card-light: #ebeae7;
    --card-teal: #466f7c;
    --brand-teal: #40707e;
    --ink: #4a4a4a;
    --paper: #f1efeb;
  }
  * { margin: 0; padding: 0; box-sizing: border-box; }
  html, body { width: 1200px; height: 900px; overflow: hidden; }
  body {
    background: var(--backdrop);
    position: relative;
    font-family: "Libre Caslon Text", Georgia, serif;
  }
  .card {
    position: absolute;
    left: 353px;
    width: 490px;
    height: 317px;
  }
  .card--front { top: 93px; background: var(--card-light); color: var(--ink); }
  .card--back { top: 457px; background: var(--card-teal); color: var(--paper); }

  .holder-name {
    position: absolute; left: 51px; top: 50px;
    font-family: "Playfair Display", Georgia, serif;
    font-weight: 600; font-size: 31px; line-height: 1;
    color: var(--brand-teal);
  }
  .holder-role {
    position: absolute; left: 51px; top: 88px;
    font-family: "Playfair Display", Georgia, serif;
    font-size: 21px; line-height: 1; color: var(--ink);
  }
  .front-brand {
    position: absolute; left: 290px; top: 62px; width: 170px;
    display: flex; align-items: center; gap: 8px;
    font-family: "Playfair Display", Georgia, serif;
    font-weight: 600; font-size: 19px; line-height: 1.1;
    color: var(--brand-teal);
  }
  .brand-dot {
    flex: none; width: 14px; height: 14px; border-radius: 50%;
    background: var(--brand-teal);
  }
  .address {
    position: absolute; left: 51px; top: 150px;
    font-style: normal; font-size: 15px; line-height: 23px;
  }
  .contact {
    position: absolute; left: 51px; top: 204px;
    list-style: none; font-size: 15px; line-height: 21px;
  }
  .contact .label { color: var(--brand-teal); }
  .website {
    position: absolute; left: 51px; top: 253px; font-size: 15px;
  }
  .website .domain { color: var(--brand-teal); }

  .back-brand {
    position: absolute; left: 0; right: 0; top: 62px;
    text-align: center;
    font-family: "Playfair Display", Georgia, serif;
    font-weight: 700; font-size: 40px; line-height: 1; letter-spacing: -0.5px;
    color: var(--paper);
  }
  .mission {
    position: absolute; left: 30px; right: 30px; top: 212px;
    text-align: center; font-size: 11.2px; line-height: 16px;
  }
  .mission p + p {
    margin-top: 8px; padding-top: 7px;
    border-top: 1px solid var(--paper);
    margin-left: 5px; margin-right: 5px;
  }
</style>
</head>
<body>
  <section class="card card--front" aria-label="Business card front">
    <h1 class="holder-name">Rowan Ellery</h1>
    <p class="holder-role">Founder &amp; CEO</p>
    <div class="front-brand"><span class="brand-dot"></span><span>Lantern and Tide</span></div>
    <address class="address">14 Harbour View Road,<br>Singapore 098765</address>
    <ul class="contact">
      <li><span class="label">P :</span> (555) 013-4420</li>
      <li><span class="label">E :</span> info@lanternandtide.com</li>
    </ul>
    <p class="website">www.<span class="domain">lanternandtide</span>.com</p>
  </section>

  <section class="card card--back" aria-label="Business card back">
    <h2 class="back-brand">Lantern and Tide</h2>
    <div class="mission">
      <p>We provide expert, personalised nutrition care to support<br>a wide range of health needs, from chronic conditions to mindful eating.</p>
      <p>Our team also offers consulting, speaking, and tailored solutions for<br>healthcare providers, organisations, and food services.</p>
    </div>
  </section>
</body>
</html>
```